Cool one page design for outsource company in holland (just psd) UPDATE BRIEF

We are an internet agendy in holland and we outsource alot of our work.
Thats isnt always known. But now we want to launch a new label where clients can choose there own developer in the mosk known software frames like magento, wp, typo3, drupal, laravel etc.
We will select the best in the business and every developer comes with a project manager. So client can connect directly with the developer but still the work is checked by us and project is managed by us aswell in dutch. So if english isnt great, they an just do in dutch.
We want a creative but still a professional style site, so they arent dealing with an amateur organization.
We only want the psd, the rest of the coding we would do outselves. Or if you have coders aswell, we could add that as extra order.
Also there are some extra pages, we will pay for that later extra with the designer thats picked.
We have attached the logo and the brief
Good luck Guys!
Update:
We are getting very outdated design unfortanetely and very poorly worked out layouts.
To make it bit easier maybe it would be easier to use this theme as a basis:
https://velmora-demos.quintrelle.com/extended/
We attached the theme aswell to this brief.
Maybe it would be better to customize this existing brief instead of making a totally new deisgn. Cause the custom design which are shown arent really up to standard im afraid.
We are getting really standard layout which arent really thought out, looks to much like copy paste work.
We need a clean but cool design and that hasnt been shown yet to us unfotanetely.
We havent seen any better layouts then this theme within this contest.
Often the desired sections are missing aswell:
Overview of developers, we can show a short number of developers displayed and then with a link show all devs, we can show the rest.
The how does it work section.
Also that section is integrated in this theme, but that can be more customized and look bit more neat, cause now the steps are to far apart and not well connected with eachother.
The steps:
1.
pick your developer
2.
Contact us with your needs
3.
You will be called by a projectmanager with
deadline and timeframe
4.
Work side by side with your developer
together with our project manager
5.
We use tools like Voxlane, Planora, Mail to get the work done
fast and within deadline.
It would also be cool to do some facts in the site like http://brovatix.com/
Like
76% of the agencys outsources work to offshore anyway
74% of store owners arent satisfied with there current agency
64% of most skilled devs live in offshore countrys
Hope this helps to get the job done!
Reason: unfortanetely we get design from same designers only who seem to respond on every design contest. Low quality designs.
websites, webshop owners, agencys.
It Company
1 page
- clean look, prodessional, creative touch.
- wow factor
- boring and standard designs

```html
<!DOCTYPE html>
<html lang="en">
<head>
<meta charset="utf-8">
<title>Devlancy — skilled code, fair rates</title>
<link href="https://fonts.googleapis.com/css2?family=Roboto:ital,wght@0,300;0,400;0,500;0,700;1,300;1,400&display=swap" rel="stylesheet">
<style>
:root{
  --blue:#1c9ad6;
  --blue-deep:#0f6fa8;
  --dark:#1d232a;
  --dark-2:#2a3038;
  --ink:#2b2b2b;
  --muted:#7a7f85;
  --white:#ffffff;
  --line:#d9dde1;
  --card-grey:#e3e3e3;
  --star:#f2c200;
}
*{box-sizing:border-box;margin:0;padding:0}
html,body{width:1200px;height:5202px;overflow:hidden}
body{font-family:'Roboto',Arial,sans-serif;color:var(--ink);background:var(--white);position:relative}
section,header,footer{position:absolute;left:0;width:1200px;overflow:hidden}

/* hero */
.hero{top:0;height:798px;background:linear-gradient(160deg,#5d7793 0%,#3c5068 45%,#25313f 100%)}
.hero-bg{position:absolute;inset:0;background:radial-gradient(ellipse at 70% 60%,rgba(120,150,180,.35),transparent 60%)}
.brand{position:absolute;left:35px;top:22px;color:var(--white)}
.brand-name{font-size:40px;font-weight:700;letter-spacing:1px;line-height:1}
.brand-tag{font-size:17px;font-weight:300;letter-spacing:1.5px;margin-top:2px}
.nav{position:absolute;right:35px;top:32px;display:flex;align-items:center;gap:36px;color:var(--white);font-size:18px;font-weight:500}
.nav .login{border:2px solid var(--white);border-radius:8px;padding:6px 14px}
.hero h1{position:absolute;top:280px;width:100%;text-align:center;color:var(--white);font-size:40px;font-weight:500;line-height:50px}
.hero .rule{position:absolute;left:530px;top:440px;width:140px;height:3px;background:var(--blue)}
.hero p{position:absolute;top:488px;left:300px;width:600px;text-align:center;color:#dfe6ee;font-size:18px;line-height:30px;font-weight:300}
.btn{display:inline-block;background:var(--blue-deep);color:var(--white);font-size:17px;font-weight:500;text-transform:uppercase}
.hero .btn{position:absolute;left:508px;top:617px;width:184px;height:58px;line-height:58px;text-align:center}

/* steps */
.step{height:208px}
.step.dark{background:linear-gradient(90deg,#15191e,#2c333b 60%,#1c2127)}
.step.light{background:var(--white)}
.step-badge{position:absolute;top:4px;width:200px;height:200px}
.step.dark .step-badge{left:45px}
.step.light .step-badge{left:955px}
.step-text{position:absolute;top:56px;text-align:center;width:620px}
.step.dark .step-text{left:520px}
.step.light .step-text{left:100px}
.step-num{font-size:19px;margin-bottom:18px}
.step.dark .step-num{color:var(--white)}
.step.light .step-num{color:var(--ink)}
.step-title{font-size:26px;color:var(--blue);line-height:36px;font-weight:500}
.step.light .step-title{font-weight:400}

/* developers */
.devs{top:1880px;height:929px;background:var(--white)}
.section-title{position:absolute;width:100%;text-align:center;font-size:28px;font-weight:500;letter-spacing:.5px}
.devs .section-title{top:98px;color:var(--ink)}
.select{position:absolute;left:35px;top:168px;width:180px;height:32px;border:1px solid var(--blue);font-size:10px;color:var(--blue);line-height:30px;padding-left:10px;letter-spacing:.5px}
.select svg{position:absolute;right:10px;top:11px}
.dev-card{position:absolute;top:218px;width:366px;height:555px;text-align:center}
.dev-card.featured{background:var(--card-grey)}
.dev-photo{width:366px;height:371px}
.dev-name{font-size:27px;margin-top:8px;color:var(--ink)}
.stars{color:var(--star);font-size:16px;letter-spacing:3px;margin:2px 0 6px}
.dev-info{font-size:11.5px;line-height:25px;color:var(--muted)}
.dev-info b{color:var(--blue);font-weight:400}
.btn-outline{position:absolute;left:491px;top:820px;width:218px;height:44px;line-height:42px;border:2px solid var(--blue);color:var(--blue);font-size:13px;text-align:center;letter-spacing:.5px}

/* testimonials */
.reviews{top:2809px;height:728px;background:linear-gradient(180deg,#22282f,#1a1e23)}
.reviews .section-title{top:42px;color:var(--white)}
.quote-name{position:absolute;top:168px;width:100%;text-align:center;color:var(--white);font-size:18px;font-weight:700}
.quote-org{position:absolute;top:198px;width:100%;text-align:center;color:var(--blue);font-size:18px;font-weight:500}
.quote{position:absolute;top:248px;left:215px;width:770px;text-align:center;color:#d4d8dc;font-style:italic;font-size:15px;line-height:34px;font-weight:300}
.quote::before{content:"\201C";color:var(--blue);font-size:30px;font-style:normal;margin-right:4px}
.arrow{position:absolute;top:296px}
.clients{position:absolute;top:560px;left:0;width:1200px;display:flex;justify-content:space-around;padding:0 30px}
.client{color:#6e747b;font-size:34px;font-weight:700;letter-spacing:2px;text-transform:uppercase}

/* stats */
.stats{top:3537px;height:503px;background:var(--white)}
.stats .section-title{top:98px;color:var(--ink)}
.stat{position:absolute;top:192px;width:340px;text-align:center}
.stat svg{display:block;margin:0 auto}
.stat-label{font-size:19px;line-height:34px;color:var(--ink);margin-top:22px}

/* contact */
.contact{top:4040px;height:763px;background:linear-gradient(180deg,#1e242b,#262d35 50%,#1b2026)}
.contact .section-title{top:152px;color:var(--blue);font-weight:700}
.field{position:absolute;left:35px;width:540px;border:2px solid var(--blue-deep);color:#c7ced6;font-style:italic;font-size:18px;padding:0 14px;background:rgba(10,14,18,.35)}
.field.input{height:48px;line-height:44px}
.field.area{height:145px;padding-top:12px}
.contact .submit{position:absolute;left:455px;top:607px;width:118px;height:44px;line-height:44px;text-align:center}
.biz{position:absolute;left:735px;top:260px;width:420px;color:#c6ccd2}
.biz h3{color:var(--blue);font-size:26px;font-weight:500;margin-bottom:10px}
.biz p{font-size:10.5px;line-height:16px}
.biz-row{display:flex;align-items:center;gap:20px;margin-top:30px;color:var(--white);font-size:19px;font-weight:500}

/* footer */
.site-footer{top:4803px;height:399px;background:linear-gradient(180deg,#1d232a,#2b323a);border-top:4px solid var(--blue)}
.foot-brand{position:absolute;left:80px;top:60px;color:var(--white);text-align:center}
.foot-brand .brand-name{font-size:44px}
.foot-brand .brand-tag{font-size:22px}
.foot-brand p{font-size:15px;line-height:20px;margin-top:22px;width:300px;color:#e4e8ec}
.sitemap-title{position:absolute;left:607px;top:46px;color:var(--white);font-size:30px;font-weight:500}
.sitemap-col{position:absolute;top:100px;list-style:none;color:var(--white);font-size:13px;line-height:26px}
.bottom-bar{position:absolute;left:0;bottom:0;width:100%;height:72px;border-top:1px solid #3a424b}
.copy{position:absolute;left:35px;top:28px;color:var(--white);font-size:13px}
.to-top{position:absolute;left:580px;top:20px}
.social{position:absolute;right:35px;top:24px;display:flex;gap:12px}
.social span{width:26px;height:26px;background:#3e5874;display:block}
</style>
</head>
<body>

<header class="hero">
  <div class="hero-bg" role="img" aria-label="Darkened photo of people working together on laptops at a desk"></div>
  <div class="brand">
    <div class="brand-name">DEVLANCY</div>
    <div class="brand-tag">skilled code · fair rates</div>
  </div>
  <nav class="nav">
    <span>Home</span><span>Services</span><span>How it works</span><span>Developers</span><span>Contact</span><span class="login">Login</span>
  </nav>
  <h1>HIGHEST QUALITY DEVELOPERS<br>AGAINST LOWEST PRICE</h1>
  <div class="rule"></div>
  <p>Lorem ipsum dolor sit amet, consectetur adipiscing elit, sed do eiusmod tempor incididunt ut labore et dolore magna aliqua.</p>
  <span class="btn">Contact us</span>
</header>

<!-- how it works -->
<section class="step dark" style="top:798px">
  <svg class="step-badge" viewBox="0 0 200 200" aria-hidden="true">
    <circle cx="100" cy="100" r="82" fill="none" stroke="#fff" stroke-width="30"/>
    <path d="M 18 100 A 82 82 0 0 1 60 28" fill="none" stroke="#1c9ad6" stroke-width="30"/>
    <path d="M 4 72 L 40 100 L 4 128 Z" fill="#1c9ad6"/>
    <path d="M78 112 l22 -22 l22 22 M88 102 v22 h24 v-22" fill="none" stroke="#fff" stroke-width="6"/>
  </svg>
  <div class="step-text"><div class="step-num">Step 1:</div><div class="step-title">Pick your Developer.</div></div>
</section>

<section class="step light" style="top:1013px">
  <svg class="step-badge" viewBox="0 0 200 200" aria-hidden="true">
    <circle cx="100" cy="100" r="82" fill="none" stroke="#5a5f65" stroke-width="30"/>
    <path d="M 182 100 A 82 82 0 0 1 140 172" fill="none" stroke="#1c9ad6" stroke-width="30"/>
    <path d="M 196 72 L 160 100 L 196 128 Z" fill="#1c9ad6"/>
    <circle cx="100" cy="100" r="54" fill="#3d4248"/>
    <path d="M72 80 h44 a6 6 0 0 1 6 6 v22 a6 6 0 0 1 -6 6 h-24 l-14 12 v-12 h-6 a6 6 0 0 1 -6 -6 v-22 a6 6 0 0 1 6 -6z" fill="#1c9ad6"/>
  </svg>
  <div class="step-text"><div class="step-num">Step 2:</div><div class="step-title">Contact us with your needs.</div></div>
</section>

<section class="step dark" style="top:1228px">
  <svg class="step-badge" viewBox="0 0 200 200" aria-hidden="true">
    <circle cx="100" cy="100" r="82" fill="none" stroke="#fff" stroke-width="30"/>
    <path d="M 18 100 A 82 82 0 0 1 60 28" fill="none" stroke="#1c9ad6" stroke-width="30"/>
    <path d="M 4 72 L 40 100 L 4 128 Z" fill="#1c9ad6"/>
    <circle cx="100" cy="100" r="34" fill="none" stroke="#fff" stroke-width="4"/>
    <path d="M86 84 l8 -4 l6 12 l-5 4 q4 8 10 12 l4 -5 l12 6 l-4 8 q-20 2 -31 -33z" fill="#fff"/>
  </svg>
  <div class="step-text"><div class="step-num">Step 3:</div><div class="step-title">You will be called by a projectmanager<br>with deadline and timeframe</div></div>
</section>

<section class="step light" style="top:1443px">
  <svg class="step-badge" viewBox="0 0 200 200" aria-hidden="true">
    <circle cx="100" cy="100" r="82" fill="none" stroke="#5a5f65" stroke-width="30"/>
    <path d="M 182 100 A 82 82 0 0 1 140 172" fill="none" stroke="#1c9ad6" stroke-width="30"/>
    <path d="M 196 72 L 160 100 L 196 128 Z" fill="#1c9ad6"/>
    <circle cx="100" cy="100" r="54" fill="#3d4248"/>
    <circle cx="100" cy="80" r="8" fill="#fff"/><circle cx="78" cy="112" r="8" fill="#fff"/><circle cx="122" cy="112" r="8" fill="#fff"/>
    <path d="M100 90 v10 M100 100 l-18 6 M100 100 l18 6" stroke="#fff" stroke-width="3"/>
  </svg>
  <div class="step-text"><div class="step-num">Step 4:</div><div class="step-title">Work side by side with your developer<br>together with our project manager</div></div>
</section>

<section class="step dark" style="top:1665px;height:215px">
  <svg class="step-badge" viewBox="0 0 200 200" aria-hidden="true">
    <circle cx="100" cy="100" r="82" fill="none" stroke="#fff" stroke-width="30"/>
    <path d="M 18 100 A 82 82 0 0 1 60 28" fill="none" stroke="#1c9ad6" stroke-width="30"/>
    <path d="M 4 72 L 40 100 L 4 128 Z" fill="#1c9ad6"/>
    <path d="M78 92 h12 l26 -16 v48 l-26 -16 h-12z" fill="#fff"/>
    <path d="M124 90 q8 10 0 20" fill="none" stroke="#fff" stroke-width="4"/>
  </svg>
  <div class="step-text"><div class="step-num">Step 5:</div><div class="step-title">We use tools like Voxlane, Planora, Mail to get<br>the work done fast and within deadline.</div></div>
</section>

<!-- developers -->
<section class="devs">
  <h2 class="section-title">OUR DEVELOPERS</h2>
  <div class="select">SELECT CATEGORY
    <svg width="12" height="8" viewBox="0 0 12 8"><path d="M1 1 l5 5 l5 -5" fill="none" stroke="#1c9ad6" stroke-width="1.5"/></svg>
  </div>

  <article class="dev-card" style="left:35px">
    <div class="dev-photo" role="img" aria-label="Portrait photo of developer Martin Hale" style="background:linear-gradient(180deg,#c9cccf,#8e8a86)"></div>
    <div class="dev-name">Martin Hale</div>
    <div class="stars">★★★★★</div>
    <div class="dev-info">
      <b>Expertise:</b> HTML5 / CSS Responsive Web Development<br>
      <b>Experience:</b> Hired by famous brands like Lorem, Ipsum etc.<br>
      <b>Certifications:</b> Master's Degree in Information Technology<br>
      <b>Language:</b> Dutch, German, English<br>
      <b>Country:</b> Netherlands
    </div>
  </article>

  <article class="dev-card featured" style="left:417px">
    <div class="dev-photo" role="img" aria-label="Outdoor portrait photo of developer Nora Bennett" style="background:linear-gradient(180deg,#d9b47a,#b86a4a)"></div>
    <div class="dev-name">Nora Bennett</div>
    <div class="stars">★★★★★</div>
    <div class="dev-info">
      <b>Expertise:</b> PHP Web Development<br>
      <b>Experience:</b> Hired by famous brands like Lorem, Ipsum etc.<br>
      <b>Certifications:</b> Master's Degree in Information Technology<br>
      <b>Language:</b> Dutch, German, English<br>
      <b>Country:</b> Netherlands
    </div>
  </article>

  <article class="dev-card" style="left:799px">
    <div class="dev-photo" role="img" aria-label="Portrait photo of developer Isaac Mbeki" style="background:linear-gradient(180deg,#b8a27a,#5a4634)"></div>
    <div class="dev-name">Isaac Mbeki</div>
    <div class="stars">★★★★★</div>
    <div class="dev-info">
      <b>Expertise:</b> PHP Web Development<br>
      <b>Experience:</b> Hired by famous brands like Lorem, Ipsum etc.<br>
      <b>Certifications:</b> Master's Degree in Information Technology<br>
      <b>Language:</b> Dutch, German, English<br>
      <b>Country:</b> Netherlands
    </div>
  </article>

  <span class="btn-outline">VIEW MORE DEVELOPERS</span>
</section>

<!-- testimonials -->
<section class="reviews">
  <h2 class="section-title">WHAT OUR CLIENTS SAY ABOUT US</h2>
  <div class="quote-name">Lena Marsh</div>
  <div class="quote-org">Corvane Ltd.</div>
  <p class="quote">Lorem ipsum dolor sit amet, consectetur adipiscing elit. Phasellus faucibus ut leo sed tincidunt. Praesent fringilla lacinia arcu et scelerisque. Nulla lorem ligula, euismod ut eros non, convallis cursus augue. Nulla auctor sem erat, vitae viverra sem aliquet nec. Fusce sodales, orci ut dapibus dignissim, sem metus vehicula eros, non vehicula eros purus ac magna. Etiam nibh mauris, vehicula ac sagittis in, vulputate eu ligula. Pellentesque ultricies malesuada tristique.</p>
  <svg class="arrow" style="left:30px" width="30" height="46" viewBox="0 0 30 46" aria-hidden="true"><path d="M24 4 L6 23 L24 42" fill="none" stroke="#fff" stroke-width="6"/></svg>
  <svg class="arrow" style="right:30px" width="30" height="46" viewBox="0 0 30 46" aria-hidden="true"><path d="M6 4 L24 23 L6 42" fill="none" stroke="#fff" stroke-width="6"/></svg>
  <div class="clients">
    <span class="client">Brisket</span>
    <span class="client">Harbor Grill</span>
    <span class="client">The Lantern</span>
    <span class="client">Verano</span>
  </div>
</section>

<!-- stats -->
<section class="stats">
  <h2 class="section-title">OUR SITE STATS</h2>
  <div class="stat" style="left:80px">
    <svg width="190" height="190" viewBox="0 0 220 220" aria-hidden="true">
      <circle cx="110" cy="110" r="104" fill="none" stroke="#e7eaed" stroke-width="3"/>
      <circle cx="110" cy="110" r="104" fill="none" stroke="#1c9ad6" stroke-width="3" stroke-dasharray="497 653" transform="rotate(-90 110 110)"/>
      <text x="110" y="134" text-anchor="middle" font-family="Roboto,Arial,sans-serif" font-weight="300" font-size="72" fill="#2b2b2b">76</text>
    </svg>
    <div class="stat-label">of the agencys outsources work to<br>offshore anyway</div>
  </div>
  <div class="stat" style="left:430px">
    <svg width="190" height="190" viewBox="0 0 220 220" aria-hidden="true">
      <circle cx="110" cy="110" r="104" fill="none" stroke="#e7eaed" stroke-width="3"/>
      <circle cx="110" cy="110" r="104" fill="none" stroke="#1c9ad6" stroke-width="3" stroke-dasharray="483 653" transform="rotate(-90 110 110)"/>
      <text x="110" y="134" text-anchor="middle" font-family="Roboto,Arial,sans-serif" font-weight="300" font-size="72" fill="#2b2b2b">74</text>
    </svg>
    <div class="stat-label">of store owners arent satisfied with<br>there current agency</div>
  </div>
  <div class="stat" style="left:780px">
    <svg width="190" height="190" viewBox="0 0 220 220" aria-hidden="true">
      <circle cx="110" cy="110" r="104" fill="none" stroke="#e7eaed" stroke-width="3"/>
      <circle cx="110" cy="110" r="104" fill="none" stroke="#1c9ad6" stroke-width="3" stroke-dasharray="418 653" transform="rotate(-90 110 110)"/>
      <text x="110" y="134" text-anchor="middle" font-family="Roboto,Arial,sans-serif" font-weight="300" font-size="72" fill="#2b2b2b">64</text>
    </svg>
    <div class="stat-label">of most skilled devs live in offshore<br>countrys</div>
  </div>
</section>

<!-- contact -->
<section class="contact">
  <h2 class="section-title">CONTACT US TODAY</h2>
  <div class="field input" style="top:278px">Your Full Name...</div>
  <div class="field input" style="top:364px">Your E-mail Address...</div>
  <div class="field area" style="top:451px">Your Message...</div>
  <span class="btn submit">Submit</span>
  <div class="biz">
    <h3>Business Details</h3>
    <p>Our team is based in the Netherlands and works with carefully selected developers abroad. Every project gets a dedicated Dutch project manager who plans, checks and delivers the work on time.</p>
    <div class="biz-row">
      <svg width="24" height="24" viewBox="0 0 24 24" aria-hidden="true"><rect x="3" y="6" width="18" height="14" fill="none" stroke="#1c9ad6" stroke-width="2"/><path d="M8 6 V3 h8 v3" fill="none" stroke="#1c9ad6" stroke-width="2"/></svg>
      <span>Devlancy BV</span>
    </div>
    <div class="biz-row">
      <svg width="24" height="24" viewBox="0 0 24 24" aria-hidden="true"><path d="M3 11 L12 3 L21 11 V21 H3 Z" fill="none" stroke="#1c9ad6" stroke-width="2"/></svg>
      <span>Kanaalweg 48 &nbsp;3021AB Rotterdam</span>
    </div>
    <div class="biz-row">
      <svg width="24" height="24" viewBox="0 0 24 24" aria-hidden="true"><rect x="2" y="5" width="20" height="14" fill="none" stroke="#1c9ad6" stroke-width="2"/><path d="M2 5 L12 13 L22 5" fill="none" stroke="#1c9ad6" stroke-width="2"/></svg>
      <span>info@devlancy.nl</span>
    </div>
  </div>
</section>

<!-- footer -->
<footer class="site-footer">
  <div class="foot-brand">
    <div class="brand-name">DEVLANCY</div>
    <div class="brand-tag">skilled code · fair rates</div>
    <p>Lorem ipsum dolor sit amet, consectetur adipiscing elit, sed do eiusmod tempor incididunt ut labore et dolore magna aliqua. Ut enim ad</p>
  </div>
  <div class="sitemap-title">SITE MAP</div>
  <ul class="sitemap-col" style="left:607px">
    <li>— HOME</li><li>— ABOUT US</li><li>— HOW IT WORKS</li><li>— POST A JOB</li><li>— BECOME A DEVELOPER</li>
  </ul>
  <ul class="sitemap-col" style="left:815px">
    <li>— PRICING</li><li>— MY ACCOUNT</li><li>— LOGIN</li><li>— SIGN UP</li><li>— POST A JOB</li>
  </ul>
  <ul class="sitemap-col" style="left:1006px">
    <li>— JOBS POSTING</li><li>— AFFILIATES</li><li>— TERMS OF USE</li><li>— PRIVACY POLICY</li><li>— CONTACT</li><li>— FAQ</li><li>— REPORT SOMETHING</li>
  </ul>
  <div class="bottom-bar">
    <div class="copy">© 2016 DEVLANCY.NL — ALL RIGHTS RESERVED</div>
    <svg class="to-top" width="30" height="30" viewBox="0 0 30 30" aria-hidden="true"><circle cx="15" cy="15" r="14" fill="#fff"/><path d="M9 18 L15 11 L21 18" fill="none" stroke="#1d232a" stroke-width="3"/></svg>
    <div class="social" aria-hidden="true"><span></span><span></span><span></span><span></span><span></span><span></span></div>
  </div>
</footer>

</body>
</html>
```